Упаковка для Bright Vega
Задание на дизайн
Приоритеты объектов в упаковке
Зонтичная марка, Знак производителя, Марка продукта, Вид продукта, Название продукта, Иллюстрация
Размеры
Опишите свою организацию или продукт и целевую аудиторию
Производство и продажа электро-, бензо-, аккумуляторного инструмента для строительства и ремонта.
Существующая упаковка .То, что хочется обновить.
Образец существующей упаковки.
Комментарии и пожелания для дизайнеров
Необходимо полностью обновить устаревший дизайн упаковки для инструмента, на примере шуруповерта. Фирменный красный цвет, а также сам логотип и сочетания цветов внутри него менять нельзя. Логотип обязательно должен присутствовать на упаковке. Название серии Zet power line должно остаться, но в любом другом виде и написании. Остальное можно менять до неузнаваемости. Фото инструмента должно быть помещено на упаковку целиком. Упаковка должна быть современной, сочной, красочной, информативной и обязательно несложно адаптивной под другие виды инструмента и форматы коробок (ушм, перфораторы, лобзики и пр.). Другие образцы наших упаковок можно легко найти в сети.

```html
<!DOCTYPE html>
<html lang="ru">
<head>
<meta charset="utf-8">
<title>Bright Vega — аккумуляторная дрель</title>
<link rel="stylesheet" href="https://fonts.googleapis.com/css2?family=Russo+One&family=Roboto+Condensed:wght@400;700&display=swap">
<style>
  :root {
    --brand-red: #d2202f;
    --deep-red: #a3131f;
    --ink: #1d1d1f;
    --grey-light: #f2f2f2;
    --grey-mid: #d6d6d8;
    --page: #e9e9ea;
    --white: #ffffff;
  }
  * { box-sizing: border-box; margin: 0; padding: 0; }
  html, body { width: 1200px; height: 915px; overflow: hidden; background: var(--page); }
  .label {
    position: absolute; left: 50px; top: 42px; width: 1100px; height: 830px;
    background: linear-gradient(160deg, var(--white) 0%, var(--grey-light) 40%, var(--grey-mid) 100%);
    overflow: hidden;
    font-family: "Roboto Condensed", sans-serif;
    color: var(--ink);
  }
  .label__shapes { position: absolute; inset: 0; }
  .brand {
    position: absolute; left: 39px; top: 185px;
    display: flex; align-items: center; gap: 14px;
    font-family: "Russo One", sans-serif; font-size: 54px; color: var(--ink);
  }
  .brand__square { width: 22px; height: 22px; background: var(--brand-red); }
  .battery-box {
    position: absolute; left: 0; top: 317px; width: 367px; height: 117px;
    background: var(--brand-red); color: var(--white);
    display: flex; align-items: center; padding-left: 39px; gap: 16px;
  }
  .battery-box__count { font-family: "Russo One", sans-serif; font-size: 88px; line-height: 1; }
  .battery-box__spec { font-family: "Russo One", sans-serif; font-size: 28px; line-height: 1.05; }
  .battery-box__note { font-size: 17px; text-transform: uppercase; letter-spacing: .5px; }
  .battery-box__word { font-family: "Russo One", sans-serif; font-size: 34px; line-height: 1; }
  .product-kind {
    position: absolute; left: 39px; top: 486px;
    font-family: "Russo One", sans-serif; text-transform: uppercase; line-height: 1.1;
  }
  .product-kind__accent { color: var(--brand-red); font-size: 40px; }
  .product-kind__main { color: var(--ink); font-size: 34px; }
  .product-name {
    position: absolute; left: 0; top: 585px; width: 598px; height: 92px;
    background: var(--brand-red); border-radius: 0 46px 46px 0;
    border: 4px solid var(--white); border-left: none;
    box-shadow: 0 0 0 3px var(--brand-red);
    display: flex; align-items: center; padding-left: 39px;
    font-family: "Russo One", sans-serif; font-size: 82px; color: var(--white); letter-spacing: 3px;
  }
  .product-code {
    position: absolute; left: 39px; top: 705px;
    font-size: 26px; letter-spacing: 1px; color: var(--ink);
  }
  .kit-count {
    position: absolute; left: 598px; top: 340px; width: 184px; height: 85px;
    background: var(--ink); clip-path: polygon(14% 0, 100% 0, 86% 100%, 0 100%);
    display: flex; align-items: center; justify-content: center;
    font-family: "Russo One", sans-serif; font-size: 66px; color: var(--white);
  }
  .kit-caption {
    position: absolute; left: 620px; top: 440px;
    font-size: 17px; font-weight: 700; text-transform: uppercase; line-height: 1.15; color: var(--ink);
  }
  .series {
    position: absolute; left: 820px; top: 14px; height: 82px;
    display: flex; align-items: center; gap: 8px; color: var(--white);
  }
  .series__tag {
    writing-mode: vertical-rl; transform: rotate(180deg);
    font-size: 14px; letter-spacing: 2px; text-transform: uppercase;
  }
  .series__name {
    font-family: "Russo One", sans-serif; font-size: 30px; line-height: 1; text-transform: uppercase;
  }
  .series__name small { display: block; font-size: 17px; letter-spacing: 4px; margin-top: 4px; }
  .tool-photo {
    position: absolute; left: 690px; top: 135px; width: 275px; height: 695px;
    border-radius: 40px 40px 12px 12px;
    background: linear-gradient(180deg, #3a3a3c 0%, var(--deep-red) 35%, var(--brand-red) 60%, #2a2a2c 100%);
  }
</style>
</head>
<body>
  <main class="label">
    <svg class="label__shapes" width="1100" height="830" viewBox="0 0 1100 830" aria-hidden="true">
      <polygon points="860,0 1100,0 1100,830 560,830" fill="var(--brand-red)"/>
      <polygon points="800,0 840,0 540,830 500,830" fill="var(--white)"/>
      <polygon points="780,0 1100,0 1100,110 740,110" fill="var(--deep-red)"/>
    </svg>

    <div class="series">
      <span class="series__tag">classic</span>
      <span class="series__name">Zet power<small>line</small></span>
    </div>

    <div class="brand">
      <span class="brand__square"></span>
      <span class="brand__name">Bright Vega</span>
    </div>

    <div class="battery-box">
      <span class="battery-box__count">2</span>
      <div>
        <div class="battery-box__spec">20 V/2.0 Ah</div>
        <div class="battery-box__note">аккумуляторные</div>
        <div class="battery-box__word">БАТАРЕИ</div>
      </div>
    </div>

    <div class="product-kind">
      <div class="product-kind__accent">Бесщеточная</div>
      <div class="product-kind__main">Аккумуляторная</div>
    </div>

    <div class="product-name">ДРЕЛЬ</div>
    <div class="product-code">VG20-PRO-BL-2B</div>

    <div class="tool-photo" role="img" aria-label="Фото аккумуляторной дрели с батареей 20 V"></div>

    <div class="kit-count">118</div>
    <div class="kit-caption">аксессуаров<br>в комплекте</div>
  </main>
</body>
</html>
```